Plastic Aesthetic and Reconstructive Surgery

I need a double sided luxurius Business Card, with a minimal, modern design focused on my job.
Besides my Name, Surname and contact information, the use of my initials (M and T) in free style combination as a logo will help.
In the one side all data written in English.
In the other side written in Greek if possible.
Please feel free to use the letter type and size you prefer.
Please use icons type and size and orientation you like.
The Name, Surname, occupation and the initials can be UV spotted.
You can use also in the background a texture or something that will make the card luxurious.
I would prefer pal colors.
Each side can have different colors or even better they can be reversed or inverted
As I have said you can use the wet sand color, light brown, dark brown, gold, light gold, white
Updates

Need extra days to review

i am waiting for some new ideas and some modifications from the designers. I need a couple of days extention of the period for the designers to post their modifications.

Target Market(s)

Patients who need a reconstructive intervention or surgery. Also people, mainly women, that they need aesthetic or cosmetic interventions to face or body

Contact Information for Business Card

Name and surname, occupation, member of an organization , mobile telephone number, Mail, Facebook and Instagram accounts

Font styles to use
Script
Other font styles liked:
• Gabriola

Colors
FFC000
F8CF3A
FAE287
FDF2CF
FEFAEE

Requirements
Must have
• A free combination of my initials (M and T) as a logo
Nice to have
• Fade out with the background colors, UV spotted of the name, initials logo
Should not have
• Address

```html
<!DOCTYPE html>
<html lang="en">
<head>
<meta charset="utf-8">
<title>Marcos Tellis — Business Card</title>
<link href="https://fonts.googleapis.com/css2?family=Montserrat:wght@300;400;500&family=Alegreya:ital,wght@0,400;1,400&family=Roboto:wght@400&display=swap" rel="stylesheet">
<style>
  :root {
    --bg: #f4f4f4;
    --sand: #a58a73;
    --sand-deep: #8f7661;
    --white: #ffffff;
    --tan: #d7b196;
    --copper: #c8835a;
    --ink: #1d1d1d;
    --rule: #c9c9c9;
    --ghost: #f2f2f2;
  }
  * { margin: 0; padding: 0; box-sizing: border-box; }
  html, body { width: 1200px; height: 2400px; overflow: hidden; background: var(--bg); }
  .canvas { position: relative; width: 1200px; height: 2400px; }

  .card {
    position: absolute; left: 147px; width: 907px; height: 519px;
    overflow: hidden; box-shadow: 0 4px 10px rgba(0,0,0,.28);
  }
  .card--front { top: 655px; background: var(--sand); }
  .card--back { top: 1226px; background: var(--white); }

  .monogram-ghost {
    position: absolute; font-family: "Montserrat", sans-serif; font-weight: 300;
    line-height: 1; white-space: nowrap;
  }
  .card--front .monogram-ghost { left: 0; top: 70px; font-size: 330px; color: var(--sand-deep); opacity: .5; }
  .card--back .monogram-ghost { left: 540px; top: 0; font-size: 430px; color: var(--ghost); }

  .brand { position: absolute; text-align: center; }
  .card--front .brand { left: 556px; top: 50px; width: 300px; }
  .card--back .brand { left: 596px; top: 38px; width: 270px; }

  .brand__mark {
    font-family: "Montserrat", sans-serif; font-weight: 300; line-height: 1;
    letter-spacing: 6px;
  }
  .card--front .brand__mark { font-size: 96px; color: var(--white); height: 150px; padding-top: 30px; }
  .card--back .brand__mark { font-size: 80px; color: var(--tan); height: 118px; padding-top: 22px; }

  .brand__name {
    font-family: "Montserrat", sans-serif; font-weight: 500; letter-spacing: 5px; white-space: nowrap;
  }
  .card--front .brand__name { font-size: 21px; color: var(--white); margin-top: 10px; }
  .card--back .brand__name { font-size: 19px; color: var(--tan); margin-top: 8px; }

  .brand__field {
    font-family: "Alegreya", serif; font-style: italic; font-size: 19px;
    line-height: 26px; color: var(--white); margin-top: 18px;
  }

  .identity { position: absolute; left: 54px; top: 238px; }
  .identity__name { font-family: "Alegreya", serif; font-size: 25px; color: var(--copper); letter-spacing: .4px; margin-bottom: 2px; }
  .identity__line { font-family: "Alegreya", serif; font-style: italic; font-size: 19px; color: var(--ink); line-height: 30px; }

  .divider { position: absolute; left: 54px; top: 370px; width: 806px; height: 1px; background: var(--rule); }

  .contact { position: absolute; left: 54px; top: 390px; list-style: none; }
  .contact li {
    display: flex; align-items: center; height: 41px;
    font-family: "Roboto", sans-serif; font-size: 21px; color: var(--ink);
  }
  .contact svg { width: 22px; height: 22px; margin-right: 18px; fill: var(--tan); }

  .social { position: absolute; left: 808px; top: 440px; display: flex; gap: 12px; }
  .social span { width: 18px; height: 18px; border-radius: 50%; background: var(--tan); }
</style>
</head>
<body>
<main class="canvas">

  <section class="card card--front" aria-label="Card front">
    <div class="monogram-ghost" aria-hidden="true">MT</div>
    <div class="brand">
      <div class="brand__mark">MT</div>
      <div class="brand__name">Dr MARCOS TELLIS</div>
      <p class="brand__field">Πλαστική Επανορθωτική και<br>Αισθητική Χειρουργική</p>
    </div>
  </section>

  <section class="card card--back" aria-label="Card back">
    <div class="monogram-ghost" aria-hidden="true">MT</div>
    <div class="brand">
      <div class="brand__mark">MT</div>
      <div class="brand__name">Dr MARCOS TELLIS</div>
    </div>

    <div class="identity">
      <p class="identity__name">ΜΑΡΚΟΣ ΤΕΛΛΗΣ, MD, MSC</p>
      <p class="identity__line">Πλαστική Επανορθωτική και Αισθητική Χειρουργική</p>
      <p class="identity__line">Μέλος Ε.Ι.Π.Χ.Α</p>
    </div>

    <div class="divider"></div>

    <ul class="contact">
      <li>
        <svg viewBox="0 0 24 24" aria-hidden="true"><path d="M6.6 10.8c1.4 2.8 3.8 5.1 6.6 6.6l2.2-2.2c.3-.3.7-.4 1-.2 1.1.4 2.3.6 3.6.6.6 0 1 .4 1 1V20c0 .6-.4 1-1 1C10.6 21 3 13.4 3 4c0-.6.4-1 1-1h3.5c.6 0 1 .4 1 1 0 1.3.2 2.5.6 3.6.1.3 0 .7-.2 1z"/></svg>
        +30 690 123 4567
      </li>
      <li>
        <svg viewBox="0 0 24 24" aria-hidden="true"><path d="M2 5h20v14H2z M3.5 6.5 12 13l8.5-6.5" fill="none" stroke="#d7b196" stroke-width="1.6"/></svg>
        marcos.tellis.md@mailbox.com
      </li>
    </ul>

    <div class="social" aria-label="Social accounts">
      <span></span><span></span>
    </div>
  </section>

</main>
</body>
</html>
```